Radio Service company needs ad for trade publication

Airwave Partners provides sales, content, production, technology, and promotion products and services to radio stations to help increase sales and solutions to improve operations and reduce costs. We are looking for a creative ad (sizes 720x250, 300x250, 728x180) with a theme around "MASTER YOUR 2024 BUDGET with AIRWAVE PARTNERS". Categories we have products/services to help them get budget into alignment. (1) Sales (2) Content & Programming (3) Technology (4) Production & Imaging (5) Promotions & Marketing (6) Support Services
"Don't go into the new year with an Unrealistic Budget.....We can Help!"

```html
<!DOCTYPE html>
<html lang="en">
<head>
<meta charset="UTF-8">
<title>Master Your 2024 Budget with Airwave Partners – Trade Ads</title>
<link href="https://fonts.googleapis.com/css2?family=Montserrat:wght@300;400;600;700&display=swap" rel="stylesheet">
<style>
  :root {
    --navy: #2a3a8c;
    --sky: #0096f5;
    --white: #ffffff;
    --page: #ffffff;
    --shadow: rgba(0, 0, 0, 0.28);
  }
  html, body {
    margin: 0;
    padding: 0;
    width: 1200px;
    height: 1200px;
    overflow: hidden;
    background: var(--page);
    font-family: "Montserrat", Arial, sans-serif;
  }
  .stage {
    position: relative;
    width: 1200px;
    height: 1200px;
  }
  .ad {
    position: absolute;
    background: var(--white);
    box-shadow: 0 30px 70px var(--shadow);
    overflow: hidden;
  }
  .ad-shapes {
    position: absolute;
    inset: 0;
    width: 100%;
    height: 100%;
  }
  .ad-text {
    position: absolute;
    margin: 0;
    line-height: 1;
    white-space: nowrap;
  }

  /* Leaderboard 720 x 250 */
  .ad-wide { left: 240px; top: 261px; width: 720px; height: 250px; }
  .ad-wide .headline-kicker {
    left: 41px; top: 82px;
    font-size: 30px; font-weight: 700; color: var(--sky); letter-spacing: -0.5px;
  }
  .ad-wide .headline-main {
    left: 41px; top: 112px;
    font-size: 41px; font-weight: 400; color: var(--white); letter-spacing: -0.5px;
  }
  .ad-wide .tagline {
    left: 41px; top: 227px;
    font-size: 14.5px; font-weight: 400; color: var(--white); letter-spacing: 0.2px;
  }
  .ad-wide .brand { position: absolute; left: 472px; top: 60px; color: var(--navy); font-weight: 600; }
  .ad-wide .brand-with { font-size: 15px; letter-spacing: 1.5px; display: block; margin-bottom: 4px; }
  .ad-wide .brand-name { display: block; font-size: 40px; line-height: 1.05; letter-spacing: -0.5px; }
  .ad-wide .brand-name-second { display: block; font-size: 30.5px; line-height: 1.1; letter-spacing: -0.5px; }

  /* Medium rectangle 300 x 250 */
  .ad-square { left: 450px; top: 644px; width: 300px; height: 250px; }
  .ad-square .headline-kicker {
    right: 20px; top: 32px;
    font-size: 31px; font-weight: 700; color: var(--sky); letter-spacing: -0.5px;
  }
  .ad-square .headline-year,
  .ad-square .headline-word {
    right: 20px;
    font-size: 42px; font-weight: 400; color: var(--navy); letter-spacing: -0.5px;
  }
  .ad-square .headline-year { top: 79px; }
  .ad-square .headline-word { top: 124px; }
  .ad-square .brand {
    position: absolute; right: 20px; top: 175px;
    text-align: left; color: var(--navy); font-weight: 600;
  }
  .ad-square .brand-with { font-size: 8px; letter-spacing: 1px; display: block; margin-bottom: 2px; }
  .ad-square .brand-name { display: block; font-size: 19px; line-height: 1.05; letter-spacing: -0.3px; }
  .ad-square .brand-name-second { display: block; font-size: 14.5px; line-height: 1.1; letter-spacing: -0.3px; }
</style>
</head>
<body>
<main class="stage">

  <section class="ad ad-wide" aria-label="720 by 250 banner">
    <svg class="ad-shapes" viewBox="0 0 720 250" aria-hidden="true">
      <polygon fill="var(--navy)" points="0,0 288,0 418,101 286,216 720,216 720,250 0,250"/>
      <polygon fill="var(--sky)" points="344,216 428,143 405,216"/>
    </svg>
    <p class="ad-text headline-kicker">MASTER YOUR</p>
    <p class="ad-text headline-main">2024 BUDGET</p>
    <div class="brand">
      <span class="brand-with">WITH</span>
      <span class="brand-name">AIRWAVE</span>
      <span class="brand-name-second">PARTNERS</span>
    </div>
    <p class="ad-text tagline">DON'T GO INTO THE NEW YEAR WITH AN UNREALISTIC BUDGET.....WE CAN HELP!</p>
  </section>

  <section class="ad ad-square" aria-label="300 by 250 banner">
    <svg class="ad-shapes" viewBox="0 0 300 250" aria-hidden="true">
      <polygon fill="var(--navy)" points="0,64 98,142 0,227"/>
      <polygon fill="var(--sky)" points="32,250 108,182 88,250"/>
    </svg>
    <p class="ad-text headline-kicker">MASTER YOUR</p>
    <p class="ad-text headline-year">2024</p>
    <p class="ad-text headline-word">BUDGET</p>
    <div class="brand">
      <span class="brand-with">WITH</span>
      <span class="brand-name">AIRWAVE</span>
      <span class="brand-name-second">PARTNERS</span>
    </div>
  </section>

</main>
</body>
</html>
```